Corvane Networks web design

Corvane is an Internet Service Provider bringing high-speed service to homes and businesses. Our principal market target is rural areas of West Michigan, but we intend to expand rapidly. We need a website to market our services, facilitate online ordering, customer support and communicate with our customers.

I will upload a draft outline of the content we hope to include in the website.

We compete directly with Halberd Communications, Lumetra, Dravix and Kelwick communications to bring Internet service to homes and businesses in our coverage area.

Our primary values include:

1. Unlike our competitors, we do not require long term contractors or service bundles; There are no termination fees, for example. All services are sold on a recurring 1-month agreement term.
2. Unlike other wireless (mobile) providers, we do not limit downloads or uploads with bit/byte buckets
3. We provide service to areas ignored by the larger carriers - Rural areas in Michigan that lack options for broadband are prime targets for Corvane to cover.
4. Unlike other wireless ISP's, we utilize licensed FCC spectrum. We do not use unlicensed/free frequencies, providing us an advantage for reliability and stability.
Updates

So many wonderful designs, thank you very much for all your hard work. We are evaluating all our favorite designs and plan to make a selection in the next 2 days. I will be in touch with you to request revisions if necessary or further refinements.  Thank you again for your efforts on this project.

Target Market(s)

Our target market is home Internet users. however, that does not mean that our users are "high tech" oriented - they are just normal mom's and pop's who buy Internet for home use. The site should be easy to navigate and communicate our message of speed, value, reliability and facilitate simple product ordering.

Industry/Entity Type

Internet

Requirements
Must have
• Our phone number should be prominently displayed 1-844-7NU-LINK
• Our logo is uploaded in the attachments.
• Design for desktop and mobile devices.
Nice to have
• The most modern of web design trends. Such as a design that facilitates parallax scrolling effects rather than lots of individual pages.
• Stock artwork communicating our values of speed and reliability.

```html
<!DOCTYPE html>
<html lang="en">
<head>
<meta charset="utf-8">
<title>Corvane Networks</title>
<link href="https://fonts.googleapis.com/css2?family=Lato:ital,wght@0,300;0,400;0,700;1,400&display=swap" rel="stylesheet">
<style>
:root{
  --orange:#f7841f;
  --orange-dark:#ef6c0c;
  --ink:#2f2f2f;
  --text:#555;
  --band:#4a4a4a;
  --band-line:#5c5c5c;
  --footer:#3c3c3c;
  --footer-bottom:#333;
  --light:#f4f4f4;
  --white:#fff;
}
*{margin:0;padding:0;box-sizing:border-box}
html,body{width:907px;height:1200px;overflow:hidden}
body{font-family:'Lato',sans-serif;color:var(--text);background:var(--white);position:relative}

/* header */
.site-header{position:absolute;top:0;left:0;width:907px;height:72px}
.brand{position:absolute;left:150px;top:18px;display:flex;align-items:center;gap:8px;font-weight:700;font-size:22px;color:var(--orange);letter-spacing:1px}
.brand-dot{width:14px;height:14px;border-radius:50%;background:var(--orange)}
.contact{position:absolute;right:155px;top:11px;display:flex;gap:14px;font-size:9.5px;font-weight:700;color:var(--ink)}
.contact span{display:flex;align-items:center;gap:5px}
.main-nav{position:absolute;right:155px;top:47px;display:flex;font-size:9px;color:var(--ink)}
.main-nav a{color:inherit;text-decoration:none;padding:0 11px;border-left:1px solid #bbb}
.main-nav a:first-child{border:0;color:var(--orange)}
.main-nav a:last-child{padding-right:0}

/* hero */
.hero{position:absolute;top:72px;left:0;width:907px;height:257px}
.hero-photo{position:absolute;inset:0;background:linear-gradient(90deg,#eef2f5 0%,#e4eaef 45%,#d9d4cf 75%,#c9b9ad 100%)}
.hero-copy{position:absolute;left:152px;top:60px}
.hero-title{font-size:38px;color:var(--ink);letter-spacing:-1.5px;line-height:1}
.hero-title b{font-weight:700}
.hero-title span{font-weight:300;font-size:32px}
.hero-sub{font-size:27px;font-weight:300;color:var(--orange);letter-spacing:-1px;margin-top:4px}
.hero-tag{font-size:14px;font-weight:300;color:var(--ink);margin-top:1px}

/* features */
.features{position:absolute;top:329px;left:0;width:907px;height:205px;background:var(--band);display:grid;grid-template-columns:350px 202px 355px;grid-template-rows:102px 103px}
.feature{display:flex;flex-direction:column;align-items:center;justify-content:flex-start;padding-top:14px;color:var(--white);font-size:12px;font-weight:400;text-align:center;border-right:1px solid var(--band-line);border-bottom:1px solid var(--band-line);line-height:1.25}
.feature:nth-child(3n){border-right:0}
.feature svg{width:46px;height:46px;margin-bottom:10px}

/* why / buy */
.values{position:absolute;top:534px;left:0;width:907px;height:212px;background:var(--light)}
.col{position:absolute;top:26px}
.col h2{font-size:20px;font-weight:400;color:var(--ink);margin-bottom:14px}
.col ul{list-style:none}
.col li{position:relative;padding-left:20px;font-size:8.3px;line-height:1.4;font-weight:400;color:#5a5a5a;margin-bottom:10px}
.col li::before{content:"";position:absolute;left:1px;top:4px;width:8px;height:8px;border-radius:50%;background:var(--orange)}
.col-why{left:152px;width:232px}
.col-buy{left:503px;width:240px}
.divider{position:absolute;left:439px;top:38px;height:144px;border-left:1px dashed #bbb}

/* feeds */
.feeds{position:absolute;top:774px;left:150px;width:606px;display:flex;justify-content:space-between}
.feed{width:195px}
.feed-bar{height:23px;background:linear-gradient(#fb9a2a,var(--orange-dark));border-radius:2px;color:var(--white);font-size:12px;display:flex;align-items:center;gap:7px;padding-left:10px;margin-bottom:9px}
.feed-bar i{width:10px;height:10px;border-radius:50%;background:var(--white);display:block}
.news p{font-size:7.8px;color:var(--ink);line-height:1.3;padding:2px 1px 6px;border-bottom:1px dashed #bbb;margin-bottom:6px}
.news p:last-child{border:0}
.tweet{display:flex;align-items:center;gap:16px;margin-bottom:14px}
.avatar{width:36px;height:36px;border-radius:50%;background:linear-gradient(#c7a48c,#8d6d5a);flex:none;border:2px solid var(--white);box-shadow:0 0 3px #bbb}
.bubble{border:1px solid #e4e4e4;border-radius:6px;padding:8px 9px;font-size:6.8px;font-style:italic;color:#444;line-height:1.3;width:126px}
.post{display:flex;gap:8px;margin-bottom:14px;padding-left:6px}
.post .avatar{border-radius:2px;width:37px;height:37px;box-shadow:none}
.post h4{font-size:8px;color:var(--ink);font-weight:700}
.post h4 small{font-weight:400;font-style:italic;font-size:6.8px;color:#555;margin-left:4px}
.post em{display:block;font-size:6.8px;color:var(--orange);margin:1px 0}
.post p{font-size:6.8px;color:#444;line-height:1.3}

/* call band */
.call{position:absolute;top:970px;left:0;width:907px;height:57px;background:linear-gradient(var(--orange-dark),#fb9428);color:var(--white);text-align:center;font-size:19.5px;font-weight:700;line-height:1.2;letter-spacing:-.6px;padding-top:5px;text-shadow:0 1px 2px rgba(0,0,0,.25)}

/* footer */
.site-footer{position:absolute;top:1027px;left:0;width:907px;height:138px;background:var(--footer);color:#bbb}
.fcol{position:absolute;top:20px;font-size:8.3px;line-height:15.2px;font-weight:300}
.fcol h5{font-size:10px;font-weight:700;color:var(--white);margin-bottom:4px;line-height:12px}
.fcol.sep{border-right:1px solid #555;padding-right:30px;height:120px}
.footer-brand{position:absolute;left:623px;top:40px;color:var(--white);font-weight:700}
.footer-brand .name{font-size:19px;letter-spacing:1px}
.footer-brand p{font-size:10px;line-height:1.3;margin-top:6px}
.footer-bottom{position:absolute;top:1165px;left:0;width:907px;height:35px;background:var(--footer-bottom);color:#bbb;font-size:8.5px;font-weight:300}
.footer-bottom .copy{position:absolute;left:152px;top:13px}
.footer-bottom nav{position:absolute;right:152px;top:13px;display:flex}
.footer-bottom a{color:#ddd;text-decoration:none;padding:0 14px;border-left:1px solid #666}
.footer-bottom a:first-child{border:0}
.footer-bottom a:last-child{padding-right:0}
</style>
</head>
<body>

<header class="site-header">
  <div class="brand"><span class="brand-dot"></span>Corvane Networks</div>
  <div class="contact">
    <span><svg width="10" height="10" viewBox="0 0 24 24"><path fill="#f7841f" d="M6.6 10.8a15 15 0 006.6 6.6l2.2-2.2c.3-.3.7-.4 1-.2 1.1.4 2.3.6 3.6.6.6 0 1 .4 1 1V20c0 .6-.4 1-1 1A17 17 0 013 4c0-.6.4-1 1-1h3.5c.6 0 1 .4 1 1 0 1.3.2 2.5.6 3.6.1.3 0 .7-.2 1z"/></svg>1-844-7NU-LINK</span>
    <span><svg width="10" height="10" viewBox="0 0 24 24"><circle cx="12" cy="7" r="5" fill="#f7841f"/><path fill="#f7841f" d="M3 22c0-5 4-8 9-8s9 3 9 8z"/></svg>517-555-0142</span>
  </div>
  <nav class="main-nav"><a href="#">Home</a><a href="#">Service Plans</a><a href="#">Coverage Map</a><a href="#">About Us</a></nav>
</header>

<section class="hero">
  <div class="hero-photo" role="img" aria-label="Photo of a woman gripping a laptop, hair blown back by the speed of the connection, in a bright office"></div>
  <div class="hero-copy">
    <h1 class="hero-title"><b>FASTER</b> <span>SPEED,</span></h1>
    <p class="hero-sub">No Limits, More Value</p>
    <p class="hero-tag">West Michigan's Best Internet Service</p>
  </div>
</section>

<section class="features">
  <div class="feature"><svg viewBox="0 0 48 48"><circle cx="24" cy="20" r="15" fill="#fff"/><circle cx="24" cy="20" r="10" fill="#f7841f"/><path d="M19 20l4 4 7-8" stroke="#fff" stroke-width="3" fill="none"/><path d="M16 32l-4 12 6-3 4 5 2-10zM32 32l4 12-6-3-4 5-2-10z" fill="#fff"/></svg>100% Satisfaction Guaranteed</div>
  <div class="feature"><svg viewBox="0 0 48 48"><text x="24" y="42" font-family="Lato,sans-serif" font-weight="700" font-size="46" fill="#fff" text-anchor="middle">$</text></svg>Honest Pricing, No Hidden Fees</div>
  <div class="feature"><svg viewBox="0 0 48 48"><path d="M10 3h20l8 8v33H10z" fill="none" stroke="#fff" stroke-width="3"/><path d="M15 16h18M15 22h18M15 28h12" stroke="#fff" stroke-width="2"/><circle cx="36" cy="38" r="7" fill="#4a4a4a" stroke="#fff" stroke-width="2.5"/><path d="M33 35l6 6M39 35l-6 6" stroke="#fff" stroke-width="2"/></svg>No Long Term Contracts</div>
  <div class="feature"><svg viewBox="0 0 48 48"><rect x="8" y="16" width="34" height="24" rx="3" fill="#fff"/><rect x="12" y="20" width="20" height="16" fill="#4a4a4a"/><path d="M18 6l7 10 7-10" stroke="#fff" stroke-width="2.5" fill="none"/><circle cx="37" cy="25" r="2" fill="#4a4a4a"/><path d="M2 40c2-8 14-8 16 0v4H2z" fill="#f7841f"/></svg>No Phone Line or Cable TV required</div>
  <div class="feature"><svg viewBox="0 0 48 48"><path d="M4 4v40h40" stroke="#fff" stroke-width="3" fill="none"/><rect x="10" y="30" width="6" height="12" fill="#fff"/><rect x="19" y="24" width="6" height="18" fill="#fff"/><rect x="28" y="28" width="6" height="14" fill="#fff"/><rect x="37" y="20" width="5" height="22" fill="#fff"/><path d="M8 24l10-10 8 6 14-14" stroke="#f7841f" stroke-width="3" fill="none"/></svg>Fast, Superior Performance</div>
  <div class="feature"><svg viewBox="0 0 48 48"><path d="M4 18a28 28 0 0140 0M10 25a19 19 0 0128 0M16 32a10 10 0 0116 0" stroke="#fff" stroke-width="4" fill="none" stroke-linecap="round"/><circle cx="24" cy="40" r="4" fill="#fff"/></svg>Interference-Free FCC Licensed<br>4G Coverage</div>
</section>

<section class="values">
  <div class="col col-why">
    <h2>Why Corvane?</h2>
    <ul>
      <li>No Download Limits! Corvane doesn't charge you more when you use more</li>
      <li>No Cancellation Fees! All services are sold on 1-month terms, there are no contract minimums and never a cancellation fee.</li>
      <li>FCC Licensed reliability. Corvane 4G utilizes the latest wireless technologies using FCC licensed frequencies. Unlike other West Michigan ISP's, our signals never fade. Enjoy stable and reliable Internet service.</li>
    </ul>
  </div>
  <div class="divider"></div>
  <div class="col col-buy">
    <h2>Buy Local</h2>
    <ul>
      <li>Corvane is Local! We're a locally owned and operated business. All of our staff live and work in Michigan. We in invest in our local community because we live it- just like you!</li>
      <li>Best Value, Best for You! Unlike cable and phone companies, we don't require you to buy everything from us. We offer the best value Internet service, and only what you want, no "bundles" required.</li>
    </ul>
  </div>
</section>

<section class="feeds">
  <div class="feed news">
    <div class="feed-bar"><i></i>Latest News Headlines</div>
    <p>Lumivox <b>Demonstrates Advanced</b> Multiscreen Video at MetroCable Summit 2014</p>
    <p>Lumivox Video Processing Selected by Northline TV for Alpine Games 2014</p>
    <p>Lumivox Streams 4K Content for <b>Multiple Screens</b> at Vistech Expo 2014</p>
    <p>Lumivox Debuts <b>Full Frame Rate Live</b> 4K HEVC Video Processing</p>
  </div>
  <div class="feed">
    <div class="feed-bar"><i></i>Latest Tweets</div>
    <div class="tweet"><div class="avatar" role="img" aria-label="Follower profile photo"></div><div class="bubble">Lorem ipsum dolor sit amet, consectetuer adipiscing elit, diam nonummy nibh euismod tiunt ut laoreet dolore.</div></div>
    <div class="tweet"><div class="avatar" role="img" aria-label="Follower profile photo"></div><div class="bubble">Lorem ipsum dolor sit amet, consectetuer adipiscing elit, diam nonummy nibh euismod tiunt ut laoreet dolore.</div></div>
  </div>
  <div class="feed">
    <div class="feed-bar"><i></i>Blog Posts</div>
    <div class="post"><div class="avatar" role="img" aria-label="Author photo"></div><div><h4>Dana Whitcombe<small>@DanaWhitcombe</small></h4><em>27-01-2014 On Monday</em><p>Consectetuer adipiscing elit, diam nonummy nibh euismod tiunt ut laoreet dolore.</p></div></div>
    <div class="post"><div class="avatar" role="img" aria-label="Author photo"></div><div><h4>Dana Whitcombe<small>@DanaWhitcombe</small></h4><em>27-01-2014 On Monday</em><p>Consectetuer adipiscing elit, diam nonummy nibh euismod tiunt ut laoreet dolore.</p></div></div>
  </div>
</section>

<section class="call">Call today to place an order or reach customer support<br>844-7NU-LINK Local number 517-555-0142</section>

<footer class="site-footer">
  <div class="fcol sep" style="left:151px"><h5>NAVIGATION</h5>Service Plans<br>Coverage Map<br>Whois Corvane<br>Company Blog<br>Customer Support<br>Account Management</div>
  <div class="fcol sep" style="left:315px"><h5>HELP</h5>Support Staff Hours<br>Weekdays 7am to 10pm<br>Weekends 8am to 5pm<br>Holiday scheduling varies</div>
  <div class="fcol sep" style="left:485px;line-height:11px"><h5 style="margin-bottom:8px">ADDRESS</h5>Corvane Networks, LLC<br>1180 Birchwood Lane<br>Grand Ledge, MI 48837</div>
  <div class="footer-brand"><div class="name">Corvane Networks</div><p>Proud to live and work in<br>Michigan!</p></div>
</footer>
<div class="footer-bottom">
  <span class="copy">Copyright © 2012. Corvane Website Outline</span>
  <nav><a href="#">Home</a><a href="#">Service Plans</a><a href="#">Coverage Map</a><a href="#">About Us</a></nav>
</div>

</body>
</html>
```